Sunscreen Package Design Modern SPF 50

Update current package design to a more modern design target women 16-40 Do not make it playful. Dune Haven is home to movie stars and high income business people PalmSprings is one of the most desired vacation areas in the world. The sun shines 350 days a year. World class Tennis and Golf tournaments are held every year with the worlds top players attending these tournaments

Target Market(s)

Women

Industry/Entity Type

Skin Protection

Font styles to use
Sans Serif

Requirements
Must have
• The words Dune Haven and VELORIMA

```html
<!DOCTYPE html>
<html lang="en">
<head>
<meta charset="utf-8">
<title>Dune Haven VELORIMA Sunscreen SPF 50</title>
<link href="https://fonts.googleapis.com/css2?family=Montserrat:wght@300;400&family=Barlow+Condensed:wght@500;600&display=swap" rel="stylesheet">
<style>
  :root {
    --backdrop: #84c54f;
    --sun-yellow: #f7e31b;
    --lime: #5fcf2f;
    --mint: #1fdca6;
    --aqua: #18dfe6;
    --sky: #22e3f7;
    --deep-teal: #12807a;
    --label-teal: #157d7e;
    --spf-yellow: #f9e21e;
    --white: #ffffff;
    --frond-dark: #3f8a2c;
    --frond-light: #6fb23e;
  }
  * { box-sizing: border-box; margin: 0; padding: 0; }
  html, body { width: 920px; height: 1200px; overflow: hidden; }
  body { background: var(--backdrop); position: relative; }

  .carton-front {
    position: absolute;
    left: 201px; top: 28px;
    width: 518px; height: 1143px;
    background:
      radial-gradient(ellipse 90% 40% at 0% 5%, var(--sun-yellow) 0%, rgba(247,227,27,0) 70%),
      linear-gradient(180deg, #d9e01c 0%, var(--lime) 22%, var(--mint) 50%, var(--aqua) 78%, var(--sky) 100%);
    border: 1px solid rgba(255,255,255,0.8);
    overflow: hidden;
  }

  .brand-mark {
    position: absolute; top: 116px; left: 0; width: 100%;
    display: flex; justify-content: center; align-items: center; gap: 10px;
    font-family: "Montserrat", sans-serif; font-weight: 400;
    font-size: 26px; letter-spacing: 4px; color: var(--white);
  }
  .brand-mark .dot { width: 16px; height: 16px; border-radius: 50%; background: var(--white); }

  .palm-frond {
    position: absolute; left: 0; top: 174px; width: 426px; height: 290px;
    background: radial-gradient(ellipse 80% 70% at 30% 35%, var(--frond-dark) 0%, var(--frond-light) 50%, rgba(111,178,62,0) 100%);
    opacity: 0.7;
  }

  .product-name {
    position: absolute; top: 480px; left: 0; width: 100%;
    text-align: center; color: var(--white);
    font-family: "Montserrat", sans-serif; font-weight: 300;
    font-size: 96px; line-height: 0.98; letter-spacing: -1px;
  }
  .product-name span { display: block; }

  .label-block { position: absolute; left: 84px; top: 704px; width: 346px; }
  .label-title {
    height: 122px; background: var(--label-teal);
    border-radius: 6px 6px 0 0; position: relative;
  }
  .label-title .line {
    position: absolute; left: 17px;
    font-family: "Montserrat", sans-serif; font-weight: 300;
    font-size: 29px; letter-spacing: 2px; color: var(--white); line-height: 1;
  }
  .label-title .line-a { top: 28px; }
  .label-title .line-b { top: 60px; }
  .label-title sup { font-size: 13px; vertical-align: top; letter-spacing: 0; }
  .spf-badge {
    position: absolute; left: 248px; top: 18px; width: 84px; height: 88px;
    background: var(--spf-yellow); border-radius: 6px;
    font-family: "Montserrat", sans-serif; color: var(--label-teal);
    text-align: center; line-height: 1;
  }
  .spf-badge .spf { display: block; font-weight: 300; font-size: 30px; margin-top: 6px; }
  .spf-badge .fifty { display: block; font-weight: 400; font-size: 50px; margin-top: -2px; }

  .label-claims {
    height: 128px; border: 1.5px solid rgba(255,255,255,0.85); border-top: none;
    text-align: center; font-family: "Barlow Condensed", sans-serif;
    padding-top: 18px;
  }
  .label-claims p { color: var(--deep-teal); font-weight: 500; font-size: 27px; letter-spacing: 2.5px; line-height: 37px; }
  .label-claims .water { color: var(--white); font-weight: 600; font-size: 22px; letter-spacing: 1.5px; line-height: 32px; }

  .net-content {
    position: absolute; top: 1024px; left: 0; width: 100%;
    text-align: center; font-family: "Barlow Condensed", sans-serif;
    font-weight: 500; font-size: 24px; letter-spacing: 1.5px; color: var(--deep-teal);
  }
</style>
</head>
<body>
  <main class="carton-front">
    <div class="brand-mark"><span class="dot"></span>VELORIMA</div>
    <div class="palm-frond" role="img" aria-label="Illustration of a green palm frond arching across the upper panel"></div>
    <h1 class="product-name"><span>Dune</span><span>Haven</span></h1>
    <section class="label-block">
      <div class="label-title">
        <span class="line line-a">VELORIMA<sup>®</sup></span>
        <span class="line line-b">SUNSCREEN</span>
        <div class="spf-badge"><span class="spf">SPF</span><span class="fifty">50</span></div>
      </div>
      <div class="label-claims">
        <p>UVA+UVB PROTECTION</p>
        <p>BROAD SPECTRUM</p>
        <p class="water">WATER RESISTANT (80 MINS)</p>
      </div>
    </section>
    <p class="net-content">3 FL OZ/88ML</p>
  </main>
</body>
</html>
```